Business Card for Luxury Hospitality Industry Career Seeker

Need something Simple, Punctual, and Elegant.

Project goal is to update phone number, layout, and wording

I look forward to working with you to create a business card I can give to managers and employers in the Luxury Hospitality industry. I want to advance a career in this industry handing out cards to managers and directors on my way up.
Updates

Updated graphics preferences in brief - would like my name flanked by small Oak, Lantern, & Key and have the Halvern 5 Star logo on the back Added Saturday, January 14, 2017

Updated Brief:-Some wording has been removed-Card Front should be more simple and tidy now-Card Back word choice & flow is improved Added Sunday, January 15, 2017

Target Market(s)

Luxury Hospitality Industry Employers and Managers

Industry/Entity Type

Hospitality

Contact Information for Business Card

(Card Front)
Dorian P. Keswick (flanked by small Oak, Lantern & Key graphic)
Luxury Hospitality
555-318-0147
fernpathmail@quillbox.net
tallyroster.net/in/dorian-keswick-rvfx-civ
My Experience = Our Success

(Card Back)
Graphic of: Halvern 5 Star logo and maybe QRT 5 Diamond Logo too
8 years military supply, logistics, & administrative experience
2 years intensive recruiting, marketing, and sales expertise
Adept problem solving, planning and management skills
5 Star, 5 Daimond, Luxury Hotels & Hospitality Rooms & Revenue

Requirements
Must have
• Name
• Phone Number
• Email Address
• Tally Roster Address
• Slogan (My Experience = Our Success)
• Graphic on back: Halvern 5 Star logo
• Qualification Remarks
• Catchy logo
Nice to have
• Background that makes a viewer think Luxury Hospitality Experience and/or World Experience
• Color combinations I've seen & liked are black & yellow, black & white, and blue & white

```html
<!DOCTYPE html>
<html lang="en">
<head>
<meta charset="utf-8">
<title>Dorian P. Keswick — Business Card</title>
<link rel="stylesheet" href="https://fonts.googleapis.com/css2?family=Cinzel:wght@500;600&family=EB+Garamond:ital,wght@0,400;1,400&display=swap">
<style>
  :root {
    --ink: #0d0d0d;
    --paper: #ffffff;
    --backdrop: #e7e4df;
    --gold: #b08a3e;
    --badge-blue: #2f4a9a;
    --muted: #3a3a3a;
  }
  * { margin: 0; padding: 0; box-sizing: border-box; }
  html, body { width: 1200px; height: 900px; overflow: hidden; }
  body {
    background: var(--backdrop);
    font-family: "EB Garamond", Georgia, serif;
    position: relative;
  }
  .card {
    position: absolute;
    left: 290px;
    width: 620px;
    height: 354px;
    border-radius: 22px;
    overflow: hidden;
    box-shadow: 0 10px 28px rgba(0,0,0,.25);
  }
  /* front */
  .card-front { top: 60px; background: var(--paper); }
  .emblem {
    position: absolute; left: 48px; top: 78px;
    width: 120px; height: 118px;
    background: var(--ink);
    border-radius: 50% 50% 46% 46%;
  }
  .identity { position: absolute; left: 190px; top: 92px; right: 30px; }
  .name {
    font-family: "Cinzel", "Times New Roman", serif;
    font-weight: 600; font-size: 42px; letter-spacing: 1.5px;
    color: var(--ink); line-height: 1;
  }
  .title {
    font-family: "Cinzel", "Times New Roman", serif;
    font-weight: 500; font-size: 14.5px; letter-spacing: .3px;
    color: var(--ink); margin-top: 8px;
  }
  .slogan {
    font-style: italic; font-size: 15px; color: var(--muted);
    text-align: right; margin-top: 6px; padding-right: 8px;
  }
  .rule-thin {
    position: absolute; left: 0; right: 0; top: 262px; height: 3px; background: var(--ink);
  }
  .contact-band {
    position: absolute; left: 0; right: 0; top: 272px; bottom: 0;
    background: var(--ink); color: var(--paper);
    display: flex; align-items: center; gap: 16px;
    padding: 0 24px; font-size: 14.5px;
  }
  .contact-item { display: flex; align-items: center; gap: 6px; white-space: nowrap; }
  .contact-icon { width: 15px; height: 15px; flex: none; }
  .network-mark { width: 13px; height: 13px; background: var(--paper); flex: none; }
  /* back */
  .card-back { top: 486px; background: var(--ink); }
  .back-panel { position: absolute; inset: 0; }
  .star-row { position: absolute; left: 200px; top: 40px; display: flex; gap: 13px; }
  .star-row svg { width: 17px; height: 17px; }
  .qualifications {
    position: absolute; left: 200px; top: 74px; right: 24px;
    list-style: none; color: var(--paper);
    font-style: italic; font-size: 19.5px; line-height: 1.32;
  }
  .badge-diamond {
    position: absolute; left: 26px; top: 196px; width: 70px; height: 46px;
    border-radius: 50%; background: var(--badge-blue);
  }
  .badge-stars {
    position: absolute; left: 40px; top: 262px; width: 70px; height: 64px;
  }
</style>
</head>
<body>

<section class="card card-front" aria-label="Business card front">
  <div class="emblem" role="img" aria-label="Oak, Lantern & Key emblem"></div>
  <div class="identity">
    <h1 class="name">DORIAN P. KESWICK</h1>
    <p class="title">RESERVATIONS AGENT HALVERN 5 STAR LUXURY HOTEL</p>
    <p class="slogan">My Experience / Our Success</p>
  </div>
  <div class="rule-thin"></div>
  <div class="contact-band">
    <span class="contact-item">
      <svg class="contact-icon" viewBox="0 0 24 24" aria-hidden="true"><path fill="#fff" d="M6.6 10.8a15 15 0 0 0 6.6 6.6l2.2-2.2c.3-.3.7-.4 1-.2 1.1.4 2.3.6 3.6.6.6 0 1 .4 1 1V20c0 .6-.4 1-1 1A17 17 0 0 1 3 4c0-.6.4-1 1-1h3.5c.6 0 1 .4 1 1 0 1.3.2 2.5.6 3.6.1.3 0 .7-.2 1z"/></svg>
      555-318-0147
    </span>
    <span class="contact-item">
      <svg class="contact-icon" viewBox="0 0 24 24" aria-hidden="true"><rect x="2" y="5" width="20" height="14" rx="2" fill="#fff"/><path d="M3 6l9 7 9-7" fill="none" stroke="#0d0d0d" stroke-width="1.8"/></svg>
      fernpathmail@quillbox.net
    </span>
    <span class="contact-item">
      <span class="network-mark" aria-hidden="true"></span>
      tallyroster.net/in/dorian-keswick-rvfx-civ
    </span>
  </div>
</section>

<section class="card card-back" aria-label="Business card back">
  <svg class="back-panel" viewBox="0 0 620 354" aria-hidden="true">
    <polygon points="0,0 40,0 150,210 150,354 0,354" fill="#ffffff"/>
    <polyline points="40,0 150,210 150,354" fill="none" stroke="#9a9a9a" stroke-width="1.5"/>
  </svg>
  <div class="star-row" aria-hidden="true">
    <svg viewBox="0 0 24 24"><path fill="#fff" d="M12 2l2.9 6.9 7.1.6-5.4 4.7 1.7 7-6.3-3.9-6.3 3.9 1.7-7L2 9.5l7.1-.6z"/></svg>
    <svg viewBox="0 0 24 24"><path fill="#fff" d="M12 2l2.9 6.9 7.1.6-5.4 4.7 1.7 7-6.3-3.9-6.3 3.9 1.7-7L2 9.5l7.1-.6z"/></svg>
    <svg viewBox="0 0 24 24"><path fill="#fff" d="M12 2l2.9 6.9 7.1.6-5.4 4.7 1.7 7-6.3-3.9-6.3 3.9 1.7-7L2 9.5l7.1-.6z"/></svg>
    <svg viewBox="0 0 24 24"><path fill="#fff" d="M12 2l2.9 6.9 7.1.6-5.4 4.7 1.7 7-6.3-3.9-6.3 3.9 1.7-7L2 9.5l7.1-.6z"/></svg>
    <svg viewBox="0 0 24 24"><path fill="#fff" d="M12 2l2.9 6.9 7.1.6-5.4 4.7 1.7 7-6.3-3.9-6.3 3.9 1.7-7L2 9.5l7.1-.6z"/></svg>
    <svg viewBox="0 0 24 24"><path fill="#fff" d="M12 2l2.9 6.9 7.1.6-5.4 4.7 1.7 7-6.3-3.9-6.3 3.9 1.7-7L2 9.5l7.1-.6z"/></svg>
    <svg viewBox="0 0 24 24"><path fill="#fff" d="M12 2l2.9 6.9 7.1.6-5.4 4.7 1.7 7-6.3-3.9-6.3 3.9 1.7-7L2 9.5l7.1-.6z"/></svg>
  </div>
  <ul class="qualifications">
    <li>8 years military supply<br>logistics, &amp; administrative experience</li>
    <li>2 years intensive recruiting<br>marketing, and sales expertise</li>
    <li>Adept problem solving<br>planning and management skills</li>
    <li>5 Star, 5 Diamond, Luxury Hotels<br>&amp; Hospitality Rooms &amp; Revenue</li>
  </ul>
  <div class="badge-diamond" role="img" aria-label="QRT 5 Diamond award badge"></div>
  <div class="badge-stars" role="img" aria-label="Halvern 5 Star award badge">
    <svg viewBox="0 0 70 64" width="70" height="64" aria-hidden="true">
      <circle cx="35" cy="32" r="30" fill="#b08a3e"/>
    </svg>
  </div>
</section>

</body>
</html>
```